Brochure

I have a current booklet for Cedar Peak Labs, I need to incorporate additional information and testing into it. attached are the current inside pages and the additional items that need to be added.

Requirements
Must have
• matching the background, colors, and format of the original inside booklet pages.

```html
<!DOCTYPE html>
<html lang="en">
<head>
<meta charset="utf-8">
<title>Antibiotic Resistance Gene – Cedar Peak Labs</title>
<link href="https://fonts.googleapis.com/css2?family=Montserrat:wght@700;800&family=Mulish:wght@400;800&display=swap" rel="stylesheet">
<style>
  :root{
    --brand-blue:#1f74c3;
    --icon-blue:#4a8fd6;
    --icon-fill:#d3e6fa;
    --ink:#1b1d22;
    --slate:#505458;
    --tab-strip:#3d4144;
    --paper:#ffffff;
  }
  *{margin:0;padding:0;box-sizing:border-box}
  html,body{width:982px;height:1200px;overflow:hidden;background:var(--paper)}
  .page{position:relative;width:982px;height:1200px;overflow:hidden;
    background:linear-gradient(100deg,#e9eaeb 0%,#ffffff 22%);
    font-family:'Mulish',sans-serif;color:var(--ink)}
  .backdrop{position:absolute;inset:0}
  .title{position:absolute;left:162px;top:134px;font-family:'Montserrat',sans-serif;
    font-weight:800;font-size:45px;line-height:48px;color:var(--brand-blue);letter-spacing:.3px}
  .feature{position:absolute;left:261px;font-size:18.5px;line-height:22px}
  .feature b{font-weight:800}
  .feature-icon{position:absolute}
  .targets{position:absolute;left:516px;width:380px;top:378px;text-align:center}
  .targets h2{font-family:'Montserrat',sans-serif;font-weight:800;font-size:24px;color:var(--brand-blue);line-height:30px}
  .targets p{font-size:17.5px;line-height:22.5px}
  .abr-box{position:absolute;left:520px;top:502px;width:372px;height:350px;border:2px solid var(--brand-blue);
    border-radius:28px;background:var(--paper);padding:20px 0 0 20px}
  .abr-box h3{font-family:'Montserrat',sans-serif;font-weight:800;font-size:16.5px;color:var(--brand-blue);line-height:22px}
  .abr-list{list-style:none;font-size:17.5px;line-height:24.2px}
  .abr-list li{position:relative;padding-left:27px}
  .abr-list li::before{content:"•";position:absolute;left:0;font-size:12px}
  .tab-strip{position:absolute;right:0;top:0;width:54px;height:1200px;background:var(--tab-strip)}
  .tab-note{position:absolute;left:956px;top:424px;transform-origin:0 0;transform:rotate(90deg) translateY(-9px);
    white-space:nowrap;font-family:'Montserrat',sans-serif;font-weight:700;font-size:15.5px;color:#fff}
  .page-number{position:absolute;left:880px;top:1156px;font-size:12.5px;color:#fff}
</style>
</head>
<body>
<div class="page">
  <svg class="backdrop" width="982" height="1200" viewBox="0 0 982 1200">
    <defs>
      <linearGradient id="labTone" x1="0" y1="0" x2="1" y2="1">
        <stop offset="0" stop-color="#cfe0ee"/>
        <stop offset="0.5" stop-color="#8fb3cf"/>
        <stop offset="1" stop-color="#3f82c9"/>
      </linearGradient>
      <radialGradient id="portraitTone" cx="0.5" cy="0.45" r="0.6">
        <stop offset="0" stop-color="#dbe8f4"/>
        <stop offset="0.75" stop-color="#eef4fa"/>
        <stop offset="1" stop-color="#ffffff" stop-opacity="0"/>
      </radialGradient>
    </defs>
    <polygon points="0,209 187,1200 0,1200" fill="var(--slate)"/>
    <polygon role="img" aria-label="Photo: gloved hand placing a sample tube into a lab dry block thermostat beside pipettes"
      points="109,789 928,699 928,1200 187,1200" fill="url(#labTone)"/>
    <rect role="img" aria-label="Photo: healthcare professional in a face mask with arms crossed"
      x="566" y="40" width="296" height="340" rx="40" fill="url(#portraitTone)"/>
  </svg>

  <h1 class="title">ANTIBIOTIC<br>RESISTANCE GENE</h1>

  <svg class="feature-icon" style="left:155px;top:272px" width="80" height="80" viewBox="0 0 80 80">
    <circle cx="40" cy="40" r="37" fill="var(--icon-fill)" stroke="var(--icon-blue)" stroke-width="2.5"/>
    <circle cx="40" cy="40" r="30" fill="none" stroke="var(--icon-blue)" stroke-width="1.5" opacity=".6"/>
    <text x="40" y="54" text-anchor="middle" font-family="Montserrat,sans-serif" font-weight="800" font-size="40" fill="var(--brand-blue)">$</text>
  </svg>
  <p class="feature" style="top:280px"><b>Cost effective</b> to help<br>maximize your lab’s<br><b>profits</b></p>

  <svg class="feature-icon" style="left:153px;top:374px" width="84" height="84" viewBox="0 0 84 84">
    <path d="M14 22 A38 38 0 1 1 6 42" fill="none" stroke="var(--icon-blue)" stroke-width="4"/>
    <circle cx="43" cy="42" r="31" fill="var(--icon-fill)" stroke="var(--icon-blue)" stroke-width="1.5"/>
    <polygon points="3,10 22,14 8,28" fill="var(--icon-fill)" stroke="var(--icon-blue)" stroke-width="2"/>
    <polyline points="48,20 37,42 48,54" fill="none" stroke="var(--brand-blue)" stroke-width="3.5" stroke-linecap="round" stroke-linejoin="round"/>
    <g fill="var(--icon-blue)"><circle cx="43" cy="16" r="1.6"/><circle cx="43" cy="68" r="1.6"/><circle cx="17" cy="42" r="1.6"/><circle cx="69" cy="42" r="1.6"/></g>
  </svg>
  <p class="feature" style="top:385px"><b>&lt;45 minute</b> run<br>time ensures <b>faster</b><br>turnaround times</p>

  <svg class="feature-icon" style="left:155px;top:484px" width="80" height="80" viewBox="0 0 80 80">
    <path d="M34 2h12v9l8 3 6-6 9 9-6 6 3 8h10v12h-10l-3 8 6 6-9 9-6-6-8 3v10H34v-10l-8-3-6 6-9-9 6-6-3-8H2V34h12l3-8-6-6 9-9 6 6 8-3z"
      fill="var(--icon-fill)" stroke="var(--icon-blue)" stroke-width="2" stroke-linejoin="round"/>
    <circle cx="40" cy="40" r="23" fill="none" stroke="var(--icon-blue)" stroke-width="2"/>
    <circle cx="40" cy="40" r="10" fill="#fff" stroke="var(--brand-blue)" stroke-width="3"/>
  </svg>
  <p class="feature" style="top:503px">Compatible with <b>ALL<br>PCR MACHINES</b></p>

  <svg class="feature-icon" style="left:157px;top:597px" width="76" height="74" viewBox="0 0 76 74">
    <g fill="var(--icon-fill)" stroke="var(--icon-blue)" stroke-width="2">
      <rect x="2" y="56" width="13" height="15"/><rect x="20" y="44" width="13" height="27"/>
      <rect x="39" y="30" width="13" height="41"/><rect x="58" y="5" width="13" height="66"/>
    </g>
    <path d="M5 34 L30 9 M18 8 H31 V21" fill="none" stroke="var(--brand-blue)" stroke-width="3" stroke-linecap="round"/>
  </svg>
  <p class="feature" style="top:601px"><b>Highly demanded</b> targets<br>to make your lab <b>more<br>appealing to providers</b></p>

  <section class="targets">
    <h2>12 TARGETS</h2>
    <p>A provider’s #1 priority is their patients.<br>When you bring them more targets, you are<br>providing them better tools for treatment</p>
  </section>

  <section class="abr-box">
    <h3>ABR</h3>
    <ul class="abr-list">
      <li>KPC – Carbapenem resistance</li>
      <li>NDM – Carbapenem resistance</li>
      <li>VIM – Carbapenem resistance</li>
      <li>IMP – Carbapenem resistance</li>
      <li>qnr – Quinolone resistance</li>
      <li>vanB – Vancomycin resistance</li>
      <li>OXA-48 – Carbapenem resistance</li>
      <li>mecA/mecC – Methicillin resistance</li>
      <li>CTX-M ESBL</li>
      <li>sul – Sulfonamide resistance</li>
      <li>vanA – Vancomycin resistance</li>
      <li>dfrA – Trimethoprim resistance</li>
    </ul>
  </section>

  <div class="tab-strip"></div>
  <div class="tab-note">Tabs Here - This portion will be trimmed off</div>
  <div class="page-number">30</div>
</div>
</body>
</html>
```